Owen Tasker Studios Business Card

Looking for a clear, modern, elegant, sharp business card that conveys a professional yet edgy image to my business as a wedding, portrait, and travel photographer. Would like something that looks vintage yet modern. Need a new business card to grow my business. We are growing the business for Wedding and Event Photography as well as fine art Photography. (Mostly Landscapes)
Updates

I’m looking through designs now but I have a new logo that i want using please.

New logo uploaded please redesign using that

PLEASE ALL DESIGNERS LOOK IN BRIEF FOR NEW LOGO

Target Market(s)

Brides, Grooms, Families with Kids, People looking for Fine Art Photography Artwork

Industry/Entity Type

Photographer

Contact Information for Business Card

Unsure

Font styles to use
Serif

Colors

Designer to choose colors to be used in the design.

Requirements
Must have
• My Website:
• http://taskerlens.examplefolio.net
• Phone:
• 323-481-5206
• Email:
• owentaskerlens@mailbox-example.net
Nice to have
• Would like a sort of shine on the printing finish.
• I like black I think it looks good on a business card.
• Can try working with my logo (png that I've attached)

```html
<!DOCTYPE html>
<html lang="en">
<head>
<meta charset="utf-8">
<title>Owen Tasker Studios – Business Card</title>
<link href="https://fonts.googleapis.com/css2?family=Source+Serif+4:opsz,wght@8..60,300;8..60,400;8..60,600&display=swap" rel="stylesheet">
<style>
  :root {
    --page: #ffffff;
    --card-front: #000000;
    --card-back: #f1f1f1;
    --ink: #111111;
    --ink-light: #ffffff;
    --shadow: rgba(0, 0, 0, 0.22);
  }
  * { margin: 0; padding: 0; box-sizing: border-box; }
  html, body {
    width: 1200px;
    height: 1200px;
    overflow: hidden;
    background: var(--page);
  }
  body {
    position: relative;
    font-family: "Source Serif 4", Georgia, serif;
    color: var(--ink);
  }
  .side-label {
    position: absolute;
    left: 194px;
    font-size: 19px;
    line-height: 1;
    font-weight: 400;
  }
  .side-label--front { top: 150px; }
  .side-label--back { top: 645px; }

  .card {
    position: absolute;
    left: 285px;
    width: 630px;
    height: 408px;
    box-shadow: 4px 5px 6px var(--shadow);
  }
  .card--front { top: 147px; background: var(--card-front); }
  .card--back { top: 642px; background: var(--card-back); }

  .brand-name {
    position: absolute;
    left: 0;
    right: 0;
    top: 180px;
    text-align: center;
    color: var(--ink-light);
    font-weight: 300;
  }
  .brand-name__main {
    display: block;
    font-size: 24px;
    line-height: 1;
    letter-spacing: 0.3em;
    padding-left: 0.3em;
  }
  .brand-name__sub {
    display: block;
    margin-top: 10px;
    font-size: 9px;
    line-height: 1;
    letter-spacing: 0.45em;
    padding-left: 0.45em;
  }

  .contact {
    position: absolute;
    right: 22px;
    top: 20px;
    text-align: right;
    font-size: 18px;
    line-height: 23px;
    font-weight: 400;
    list-style: none;
  }

  .social {
    position: absolute;
    right: 22px;
    bottom: 20px;
    text-align: right;
    font-size: 15px;
    line-height: 26px;
  }
  .social__follow { display: flex; justify-content: flex-end; align-items: center; gap: 8px; }
  .social__mark {
    width: 12px;
    height: 12px;
    background: var(--ink);
    border-radius: 2px;
  }
  .social__tagline { font-weight: 600; }
</style>
</head>
<body>
  <span class="side-label side-label--front">Front</span>
  <section class="card card--front">
    <h1 class="brand-name">
      <span class="brand-name__main">OWEN TASKER</span>
      <span class="brand-name__sub">STUDIOS</span>
    </h1>
  </section>

  <span class="side-label side-label--back">Back</span>
  <section class="card card--back">
    <ul class="contact">
      <li>owentaskerlens@mailbox-example.net</li>
      <li>323-481-5206</li>
      <li>http://taskerlens.examplefolio.net</li>
    </ul>
    <div class="social">
      <p class="social__follow">Follow us on Pictogrid <span class="social__mark"></span></p>
      <p class="social__tagline">Photographer + Galleries</p>
    </div>
  </section>
</body>
</html>
```